Neon Lodging Offers Website looking for new design

We are a online travel discounter based around hotel accommodations in Las Vegas. We need a wordpress design that will be used as our corporate cover page, and also for the affiliate pages. The current design can be viewed at http://postweaveforum.com/clients/neonoffer/ and the final design needs to include most of the navigation components. The affiliate pages will need a space to display the booking engine, for example, as shown at http://www.qrv.travel/marcoti. Our general color scheme is red/black, and the two logos we use are attached.

Because this is a crowded niche it is extremely important that we set ourselves apart in the design. The more visually stunning and out of the box the design, the better. The site needs to look distinctively different than anything else online. Since the overall layout is very basic and does not have to provide a lot of information, it leaves a lot of flexibility in design concepts.

We realize it is a truncated timetable, which is why the increased fee for your time and guaranteed payout.

Industry/Entity Type

Travel

```html
<!DOCTYPE html>
<html lang="en">
<head>
<meta charset="utf-8">
<title>Neon Lodging Offers</title>
<link href="https://fonts.googleapis.com/css2?family=Source+Sans+3:wght@400;600&display=swap" rel="stylesheet">
<style>
:root{
  --cream:#ffffc8;
  --red:#9b0a0f;
  --red-text:#a0121a;
  --panel:rgba(170,20,30,.72);
  --dark:#1c1c1c;
  --darker:#141414;
  --grey:#8a8a8a;
  --social:#3b7bc4;
}
*{margin:0;padding:0;box-sizing:border-box}
html,body{width:819px;height:1200px;overflow:hidden}
body{position:relative;background:var(--cream);font-family:"Source Sans 3",sans-serif;color:var(--red-text)}
.abs{position:absolute}
.header{left:0;top:0;width:819px;height:130px;background:var(--red)}
.brand{left:0;top:0;width:186px;height:130px;background:var(--cream);display:flex;flex-direction:column;align-items:center;justify-content:center;gap:8px}
.brand-dot{width:34px;height:34px;border-radius:50%;background:var(--red)}
.brand-name{font-size:14px;color:var(--red-text);font-weight:400}
.nav{left:206px;top:51px;display:flex;list-style:none}
.nav li{color:#fff;font-size:16.5px;padding:0 17px;line-height:28px;border-left:1px solid #f0d0d0}
.nav li:first-child{border-left:none}
.hero{left:0;top:130px;width:819px;height:367px;background:linear-gradient(135deg,#7a5a30 0%,#c9a56a 35%,#e8d3a0 55%,#a88850 80%,#5e4a2c 100%)}
.search{left:22px;top:159px;width:266px;height:310px;background:var(--panel);border-radius:10px;color:#fff}
.search .t{font-size:19px}
.search .l{font-size:14px}
.field{background:var(--cream);height:21px}
.btn{background:var(--cream);color:var(--red-text);font-size:18px;display:flex;align-items:center;justify-content:center;border-radius:3px}
.pkg-img{left:20px;width:140px;height:106px}
.pkg-title{font-size:21px;left:176px}
.pkg-price{font-size:15px;right:341px}
.pkg-desc{font-size:14.5px;left:177px}
.pkg-buy{font-size:15px;right:341px}
.rule{left:20px;width:460px;height:1.5px;background:#3a2a20}
.tm-head{left:500px;top:524px;font-size:20px}
.avatar{left:500px;width:48px;height:42px;background:radial-gradient(circle,#ff8a20,#d8320c 70%)}
.tm-name{left:560px;font-size:14px}
.tm-box{left:500px;width:299px;height:105px;background:var(--grey);color:#fff;font-size:10.5px;line-height:13.5px;padding:17px 15px 0}
.footer{left:0;top:949px;width:819px;height:213px;background:var(--dark)}
.foot-head{font-size:20px;color:var(--cream);text-decoration:underline;text-underline-offset:3px}
.foot-label{left:21px;font-size:11px;color:var(--cream)}
.foot-field{left:101px;width:169px;background:var(--cream)}
.foot-btn{left:176px;top:1133px;width:95px;height:19px;background:var(--cream);color:var(--red-text);font-size:11.5px;display:flex;align-items:center;justify-content:center;border-radius:3px}
.contact-line{left:501px;font-size:15.5px;color:var(--cream)}
.social{width:24px;height:24px;background:var(--social);top:1110px}
.bottom{left:0;top:1162px;width:819px;height:38px;background:var(--darker);color:var(--cream)}
.bottom span{position:absolute;top:9px;font-size:15px}
</style>
</head>
<body>
<header class="abs header">
  <div class="abs brand">
    <span class="brand-dot"></span>
    <span class="brand-name">Neon Lodging Offers</span>
  </div>
  <ul class="abs nav">
    <li>Home</li><li>Groups</li><li>Search events</li><li>Contact info</li><li>Register</li><li>Login</li>
  </ul>
</header>

<section class="abs hero" role="img" aria-label="Photo of an elegant hotel suite with sofas, armchairs and lamps"></section>

<form class="abs search">
  <span class="abs t" style="left:82px;top:15px">Hotel Search</span>
  <span class="abs l" style="left:18px;top:56px">City</span>
  <span class="abs field" style="left:18px;top:75px;width:231px"></span>
  <span class="abs l" style="left:18px;top:124px">Check In Date</span>
  <span class="abs l" style="left:150px;top:124px">Check Out Date</span>
  <span class="abs field" style="left:18px;top:145px;width:99px"></span>
  <span class="abs field" style="left:150px;top:145px;width:99px"></span>
  <span class="abs l" style="left:18px;top:192px">Adults</span>
  <span class="abs l" style="left:106px;top:192px">Children</span>
  <span class="abs l" style="left:196px;top:192px">Room</span>
  <span class="abs field" style="left:18px;top:215px;width:53px"></span>
  <span class="abs field" style="left:105px;top:215px;width:53px"></span>
  <span class="abs field" style="left:196px;top:215px;width:53px"></span>
  <span class="abs btn" style="left:70px;top:266px;width:122px;height:28px">Search</span>
</form>

<div class="abs pkg-img" style="top:528px;background:linear-gradient(135deg,#c9a040,#8a5a28 60%,#5a2a18)" role="img" aria-label="Hotel bedroom with four-poster bed"></div>
<span class="abs pkg-title" style="top:522px">Package 1</span>
<span class="abs pkg-price" style="top:524px">Price $200</span>
<span class="abs pkg-desc" style="top:570px">Calm Surroundings, Clean Room, Hotel Bus</span>
<span class="abs pkg-buy" style="top:616px">Buy Now</span>
<div class="abs rule" style="top:650px"></div>

<div class="abs pkg-img" style="top:666px;background:linear-gradient(135deg,#e8d8b0,#c8a878 60%,#8a6a48)" role="img" aria-label="Hotel lounge with sofas"></div>
<span class="abs pkg-title" style="top:660px">Package 2</span>
<span class="abs pkg-price" style="top:662px">Price $300</span>
<span class="abs pkg-desc" style="top:708px">Calm Surroundings, Clean Room, Hotel Bus</span>
<span class="abs pkg-buy" style="top:754px">Buy Now</span>
<div class="abs rule" style="top:789px"></div>

<div class="abs pkg-img" style="top:805px;background:linear-gradient(180deg,#3a4a78,#6a6a80 45%,#b07a40 80%,#4a2a18)" role="img" aria-label="Rooftop terrace with city skyline at dusk"></div>
<span class="abs pkg-title" style="top:798px">Package 3</span>
<span class="abs pkg-price" style="top:800px">Price $400</span>
<span class="abs pkg-desc" style="top:846px">Calm Surroundings, Clean Room, Hotel Bus</span>
<span class="abs pkg-buy" style="top:892px">Buy Now</span>

<h2 class="abs tm-head" style="font-weight:400">Testimonials</h2>
<div class="abs avatar" style="top:566px" role="img" aria-label="Orange flower"></div>
<span class="abs tm-name" style="top:567px">Marla Quinn</span>
<p class="abs tm-box" style="top:621px">"Lorem ipsum dolor sit amet, consectetur adipiscing elit, sed do eiusmod tempor incididunt ut labore et dolore magna aliqua. Ut enim ad minim veniam, quis nostrud exercitation ullamco laboris nisi ut aliquip ex ea commodo consequat laborum."</p>
<div class="abs avatar" style="top:750px" role="img" aria-label="Orange flower"></div>
<span class="abs tm-name" style="top:750px">Marla Quinn</span>
<p class="abs tm-box" style="top:804px;padding-top:24px">"Lorem ipsum dolor sit amet, consectetur adipiscing elit, sed do eiusmod tempor incididunt ut labore et dolore magna aliqua. Ut enim ad minim veniam, quis nostrud exercitation ullamco laboris nisi ut aliquip ex ea commodo consequat laborum."</p>

<footer class="abs footer"></footer>
<span class="abs foot-head" style="left:21px;top:958px">Need Help?</span>
<span class="abs foot-label" style="top:996px">Name:</span>
<span class="abs foot-field" style="top:996px;height:16px"></span>
<span class="abs foot-label" style="top:1025px">Email:</span>
<span class="abs foot-field" style="top:1025px;height:16px"></span>
<span class="abs foot-label" style="top:1058px">Message:</span>
<span class="abs foot-field" style="top:1058px;height:64px"></span>
<span class="abs foot-btn">Contact Us</span>

<span class="abs foot-head" style="left:501px;top:958px">Contact Us Today</span>
<span class="abs contact-line" style="top:998px">Name: Helen R. Osgood</span>
<span class="abs contact-line" style="top:1036px">Email: HelenROsgood@inboxly.net</span>
<span class="abs contact-line" style="top:1073px">Phone: 555-014-2290</span>
<span class="abs contact-line" style="top:1111px">Connect:</span>
<span class="abs social" style="left:571px" aria-label="Social link"></span>
<span class="abs social" style="left:603px" aria-label="Social link"></span>
<span class="abs social" style="left:635px" aria-label="Social link"></span>

<div class="abs bottom">
  <span style="left:19px;font-size:16px;top:8px">Copy Rights Reserved</span>
  <span style="left:502px">Terms &amp; Conditions</span>
  <span style="left:667px">Login</span>
  <span style="left:742px">Register</span>
</div>
</body>
</html>
```